Pest Control Flyer

I need a non tri fold flyer that will be placed door to door about 9 in long and 4 in wide. My company name is Copper Ridge Pest and Termite.
phone number is 555-214-3960. Company theme is RED WHITE & BLUE
we do guarantee our services, (dont say anything about money back guarantee ) Leave area rep / rout manager blank so we can write in it. Please add our number.
local family owned company
Services pest control, rodent control, termite treatments, mosquito services , German Roach clean outs and many more!
Discounted pricing for new customers and referrals get up to $100.00 off your initial pest control service

```html
<!DOCTYPE html>
<html lang="en">
<head>
<meta charset="UTF-8">
<title>Copper Ridge Pest &amp; Termite – Door Flyer</title>
<link rel="stylesheet" href="https://fonts.googleapis.com/css2?family=Poppins:wght@500;600;700;800&family=Roboto+Condensed:ital,wght@1,700&family=Playfair+Display:ital,wght@1,500&display=swap">
<style>
  :root {
    --navy: #1b4a93;
    --navy-deep: #163f80;
    --red: #c8202e;
    --red-bright: #e0262f;
    --ink: #3a3a3a;
    --mist: #ececec;
    --white: #ffffff;
    --stage: #6e6e6e;
  }
  * { margin: 0; padding: 0; box-sizing: border-box; }
  html, body { width: 680px; height: 1200px; overflow: hidden; }
  body {
    background: var(--stage);
    font-family: "Poppins", sans-serif;
    position: relative;
  }
  .flyer {
    position: absolute;
    left: 88px; top: 34px;
    width: 504px; height: 1132px;
    background: linear-gradient(90deg, #e6e6e6 0%, #f8f8f8 50%, #e6e6e6 100%);
    overflow: hidden;
  }
  .flyer > * { position: absolute; }
  .header-bg { left: 0; top: 0; width: 504px; height: 230px; background: var(--white); }
  .crew-illustration {
    left: 170px; top: 78px; width: 334px; height: 130px;
    background: linear-gradient(120deg, #f4e6a8 0%, #f3d36a 45%, #e7dcc0 75%, #f2b7c0 100%);
    border-radius: 6px 6px 0 0;
    opacity: .85;
  }
  .bands { left: 0; top: 0; width: 504px; height: 1132px; }
  .brand {
    left: 10px; top: 42px; width: 154px;
    text-align: center;
    color: var(--navy);
    font-weight: 700;
    font-size: 15px;
    line-height: 1.25;
  }
  .brand-dot {
    display: block; width: 44px; height: 44px; border-radius: 50%;
    background: var(--navy); margin: 0 auto 10px;
  }
  .promises {
    left: 171px; top: 28px;
    font-family: "Roboto Condensed", sans-serif;
    font-style: italic; font-weight: 700; font-size: 17px; line-height: 23px;
    z-index: 2;
  }
  .promises li { list-style: none; display: flex; align-items: center; gap: 5px; }
  .promises .blue { color: var(--navy); }
  .promises .red { color: var(--red); }
  .headline {
    left: 0; width: 504px; top: 248px;
    text-align: center;
    color: var(--white);
    font-weight: 800;
    font-size: 60px;
    line-height: 51px;
    letter-spacing: -1.5px;
  }
  .perks {
    left: 38px; top: 413px; width: 433px; height: 37px;
    background: linear-gradient(90deg, #a81722, var(--red-bright) 50%, #a81722);
    border-radius: 19px;
    display: flex; justify-content: center; align-items: center; gap: 14px;
    color: var(--white); font-weight: 600; font-size: 16px;
  }
  .perks span { display: flex; align-items: center; gap: 5px; }
  .section-title {
    left: 0; width: 504px; top: 516px;
    text-align: center; color: var(--ink);
    font-weight: 700; font-size: 22px; letter-spacing: 6.5px;
  }
  .service { width: 140px; text-align: center; color: var(--ink); font-weight: 600; font-size: 14.5px; line-height: 19px; }
  .service svg { display: block; margin: 0 auto 8px; }
  .divider { width: 0; border-left: 1.5px dashed var(--navy); }
  .offer {
    left: 34px; top: 839px; width: 443px; height: 170px;
    background: var(--red);
    border-radius: 28px 28px 0 0;
    text-align: center; color: var(--white);
    z-index: 1;
  }
  .offer-kicker { margin-top: 17px; font-weight: 800; font-size: 18px; letter-spacing: -.3px; }
  .offer-amount { margin-top: 0; font-weight: 800; font-size: 43px; line-height: 48px; letter-spacing: -1.5px; }
  .offer-detail { margin-top: 2px; font-weight: 800; font-size: 18px; letter-spacing: -.3px; }
  .footer-curve { left: 0; top: 0; width: 504px; height: 1132px; z-index: 2; }
  .contact-line {
    left: 0; width: 504px; top: 990px; z-index: 3;
    text-align: center; font-family: "Playfair Display", serif;
    font-style: italic; font-weight: 500; font-size: 25px; color: var(--ink);
  }
  .rep-field { left: 42px; z-index: 3; font-weight: 600; font-size: 15.5px; color: var(--ink); letter-spacing: -.3px; }
  .rep-field.manager { top: 1042px; }
  .rep-field.phone { top: 1074px; display: flex; align-items: center; gap: 14px; }
  .phone-number { display: flex; align-items: center; gap: 4px; color: var(--red); font-weight: 600; font-size: 22px; }
</style>
</head>
<body>
<main class="flyer">
  <div class="header-bg"></div>

  <div class="crew-illustration" role="img" aria-label="Illustration of pest control technicians in yellow protective suits spraying, beside a service van with a giant spray can on its roof"></div>

  <svg class="bands" viewBox="0 0 504 1132" aria-hidden="true">
    <path d="M0 189 Q252 233 504 189 L504 520 Q252 447 0 520 Z" fill="var(--navy)"/>
    <path d="M0 185 Q252 229 504 185" fill="none" stroke="var(--red)" stroke-width="3"/>
    <path d="M0 521 Q252 445 504 521" fill="none" stroke="var(--red)" stroke-width="4"/>
    <path d="M0 524 Q252 452 504 524 L504 530 Q252 458 0 530 Z" fill="#eeeeee"/>
  </svg>

  <div class="brand">
    <span class="brand-dot"></span>
    COPPER RIDGE<br>PEST &amp; TERMITE
  </div>

  <ul class="promises">
    <li>
      <svg width="15" height="16" viewBox="0 0 15 16"><path d="M7.5 0 L15 3 V8 C15 12 11 15 7.5 16 C4 15 0 12 0 8 V3 Z" fill="var(--navy)"/><path d="M4 8 L6.5 10.5 L11 5.5" fill="none" stroke="#fff" stroke-width="2"/></svg>
      <span><span class="blue">Guaranteed</span> <span class="red">Service</span></span>
    </li>
    <li>
      <svg width="15" height="16" viewBox="0 0 15 16"><path d="M7.5 0 L15 3 V8 C15 12 11 15 7.5 16 C4 15 0 12 0 8 V3 Z" fill="var(--navy)"/><path d="M4 8 L6.5 10.5 L11 5.5" fill="none" stroke="#fff" stroke-width="2"/></svg>
      <span><span class="red">Family owned</span> <span class="blue">company</span></span>
    </li>
  </ul>

  <h1 class="headline">PROTECTING<br>TEXAS HOMES<br>&amp; BUSINESSES</h1>

  <div class="perks">
    <span><svg width="18" height="18" viewBox="0 0 18 18"><circle cx="9" cy="9" r="7.5" fill="none" stroke="#fff" stroke-width="1.8"/><path d="M5 9 L8 12 L15 3" fill="none" stroke="#fff" stroke-width="2"/></svg>Fast</span>
    <span><svg width="18" height="18" viewBox="0 0 18 18"><circle cx="9" cy="9" r="7.5" fill="none" stroke="#fff" stroke-width="1.8"/><path d="M5 9 L8 12 L15 3" fill="none" stroke="#fff" stroke-width="2"/></svg>Reliable</span>
    <span><svg width="18" height="18" viewBox="0 0 18 18"><circle cx="9" cy="9" r="7.5" fill="none" stroke="#fff" stroke-width="1.8"/><path d="M5 9 L8 12 L15 3" fill="none" stroke="#fff" stroke-width="2"/></svg>Pest Control That Works</span>
  </div>

  <h2 class="section-title">OUR SERVICE</h2>

  <div class="service" style="left:30px; top:560px;">
    <svg width="88" height="88" viewBox="0 0 88 88" role="img" aria-label="Insect with prohibition sign"><circle cx="44" cy="44" r="44" fill="var(--navy)"/><circle cx="44" cy="44" r="29" fill="none" stroke="#fff" stroke-width="3"/><path d="M24 24 L64 64" stroke="#fff" stroke-width="3"/></svg>
    Pest control
  </div>
  <div class="divider" style="left:185px; top:565px; height:107px;"></div>
  <div class="service" style="left:185px; top:560px;">
    <svg width="88" height="88" viewBox="0 0 88 88" role="img" aria-label="Termite with prohibition sign"><circle cx="44" cy="44" r="44" fill="var(--navy)"/><circle cx="44" cy="44" r="29" fill="none" stroke="#fff" stroke-width="3"/><path d="M24 24 L64 64" stroke="#fff" stroke-width="3"/></svg>
    Termite<br>treatments
  </div>
  <div class="divider" style="left:327px; top:565px; height:107px;"></div>
  <div class="service" style="left:328px; top:560px;">
    <svg width="88" height="88" viewBox="0 0 88 88" role="img" aria-label="Rodent with prohibition sign"><circle cx="44" cy="44" r="44" fill="var(--navy)"/><circle cx="44" cy="44" r="29" fill="none" stroke="#fff" stroke-width="3"/><path d="M24 24 L64 64" stroke="#fff" stroke-width="3"/></svg>
    Rodent control
  </div>

  <div class="service" style="left:91px; top:695px;">
    <svg width="88" height="88" viewBox="0 0 88 88" role="img" aria-label="Mosquito with prohibition sign"><circle cx="44" cy="44" r="44" fill="var(--navy)"/><circle cx="44" cy="44" r="29" fill="none" stroke="#fff" stroke-width="3"/><path d="M24 24 L64 64" stroke="#fff" stroke-width="3"/></svg>
    Mosquito services
  </div>
  <div class="divider" style="left:256px; top:711px; height:104px;"></div>
  <div class="service" style="left:276px; top:695px;">
    <svg width="88" height="88" viewBox="0 0 88 88" role="img" aria-label="Cockroach with prohibition sign"><circle cx="44" cy="44" r="44" fill="var(--navy)"/><circle cx="44" cy="44" r="29" fill="none" stroke="#fff" stroke-width="3"/><path d="M24 24 L64 64" stroke="#fff" stroke-width="3"/></svg>
    German Roach<br>clean outs
  </div>

  <section class="offer">
    <p class="offer-kicker">NEW CUSTOMERS AND REFERRALS</p>
    <p class="offer-amount">GET UP TO $100 OFF</p>
    <p class="offer-detail">YOUR INITIAL PEST CONTROL SERVICE</p>
  </section>

  <svg class="footer-curve" viewBox="0 0 504 1132" aria-hidden="true">
    <path d="M0 1012 Q252 955 504 1012" fill="none" stroke="var(--red)" stroke-width="5"/>
    <path d="M0 1016 Q252 959 504 1016 L504 1132 L0 1132 Z" fill="var(--white)"/>
  </svg>

  <p class="contact-line">Contact&nbsp; Your Pest Professional</p>

  <p class="rep-field manager">Route Manager:</p>
  <p class="rep-field phone">Phone Number:
    <span class="phone-number">
      <svg width="16" height="20" viewBox="0 0 16 20"><path d="M4 1 L7 5 L5 7.5 C6 11 8 13.5 10.5 15 L13 13 L16 16.5 L13.5 19.5 C6 18 1 10 1.5 3.5 Z" fill="var(--red)"/></svg>
      555-214-3960
    </span>
  </p>
</main>
</body>
</html>
```